Salon website

Need a web design for a new blow dry and hair extension boutique in CT
would like the color scheme to be gray, white and tiffany blue
Create a web site with about 4 pages showing
1 about us page
1 blow dry services page
1 hair extension services page
1 contact us page
1 membership page
1 parties page

Industry/Entity Type

Boutique

Colors
86cfc6
cfeae6
33b7a4
aaaaaa
cbcbcb
ffffff

```html
<!DOCTYPE html>
<html lang="en">
<head>
<meta charset="utf-8">
<title>Blow Dry and Hair Extension Boutique</title>
<link rel="stylesheet" href="https://fonts.googleapis.com/css2?family=PT+Sans:ital,wght@0,400;0,700;1,400&display=swap">
<style>
  :root {
    --canvas: #ffffff;
    --hero-bg: #e6e6e6;
    --panel-grey: rgba(104, 104, 104, 0.88);
    --tiffany: #33b7a4;
    --tiffany-heading: #1cb5ab;
    --tiffany-box: rgba(58, 196, 188, 0.88);
    --nav-active: #4a4a4a;
    --white: #ffffff;
    --footer-bg: #e6e6e6;
    --footer-text: #6a6a6a;
  }
  * { margin: 0; padding: 0; box-sizing: border-box; }
  html, body {
    width: 1200px; height: 989px; overflow: hidden;
    background: var(--canvas);
    font-family: "PT Sans", Arial, sans-serif;
  }
  .page { position: relative; width: 1200px; height: 989px; }

  .hero {
    position: absolute; left: 0; top: 0; width: 1200px; height: 823px;
    background: var(--hero-bg); overflow: hidden;
  }
  .hero-photo {
    position: absolute; left: 440px; top: 30px; width: 520px; height: 793px;
    border-radius: 220px 200px 0 0;
    background: linear-gradient(100deg, #c9a796 0%, #8a6252 22%, #2a2a30 40%, #1c1c22 70%, #3a3a40 100%);
  }

  .about-panel {
    position: absolute; left: 0; top: 206px; width: 598px; height: 341px;
    background: var(--panel-grey);
  }
  .about-title {
    position: absolute; left: 211px; top: 189px;
    font-size: 39px; font-weight: 700; line-height: 44px;
    color: var(--tiffany-heading); letter-spacing: 0.2px;
  }
  .about-copy {
    position: absolute; left: 262px; top: 246px; width: 300px;
    font-size: 14px; line-height: 18.3px; color: var(--white);
  }
  .about-copy p + p { margin-top: 18.3px; }

  .brand-box {
    position: absolute; left: 624px; top: 206px; width: 325px; height: 129px;
    background: var(--tiffany-box);
  }
  .brand-title {
    position: absolute; left: 630px; top: 193px;
    font-size: 38px; font-weight: 700; line-height: 36px;
    color: var(--white);
  }
  .main-nav {
    position: absolute; left: 636px; top: 318px;
    display: flex; gap: 18px;
    font-size: 14px; list-style: none;
  }
  .main-nav a { color: var(--white); text-decoration: none; }
  .main-nav .is-active a { color: var(--nav-active); }

  .site-footer {
    position: absolute; left: 0; top: 857px; width: 595px; height: 132px;
    background: var(--footer-bg);
  }
  .footer-col { position: absolute; top: 870px; font-size: 14px; }
  .footer-col h2 {
    font-size: 14px; font-weight: 400; color: var(--tiffany);
    line-height: 18px; margin-bottom: 8px;
  }
  .footer-col p {
    font-style: italic; color: var(--footer-text); line-height: 14.6px;
  }
  .footer-col p + p { margin-top: 14.6px; }
  .footer-services { left: 261px; }
  .footer-services p { padding-left: 1px; }
  .footer-contact { left: 421px; }
</style>
</head>
<body>
<div class="page">
  <section class="hero">
    <div class="hero-photo" role="img" aria-label="Side profile of a woman with long, straight, glossy dark hair"></div>
    <div class="about-panel"></div>
    <div class="brand-box"></div>
  </section>

  <h2 class="about-title">HAIR EXTENSION</h2>
  <div class="about-copy">
    <p>Indulge your self with our personal touch, exceptional expertise and imaginative innovation at our Salon in CT. We offer a personal, friendly approach to styling, coloring and cutting your hair.</p>
    <p>Besides the basics, we have products that will improve the condition and texture of your hair with results that will amaze you. Our highly trained staff of stylists and master colorists are at the forefront of today's color and cut techniques. To match their skill, we use only the best hair treatment products. Our stylists use true techniques as the foundation of their craft, while constantly searching for the new and improved processes.</p>
  </div>

  <h1 class="brand-title">BLOW DRY AND<br>HAIR EXTENSION<br>BOUTIQUE</h1>
  <ul class="main-nav">
    <li class="is-active"><a href="#about">About us</a></li>
    <li><a href="#blow-dry">Bow Dry</a></li>
    <li><a href="#extensions">Hair Extention</a></li>
    <li><a href="#contact">Contact us</a></li>
  </ul>

  <footer class="site-footer"></footer>
  <div class="footer-col footer-services">
    <h2>Services</h2>
    <p>Bow Dry<br>Hair Extensions</p>
    <p>About Us<br>Contact Us</p>
  </div>
  <div class="footer-col footer-contact">
    <h2>Where to find us</h2>
    <p>1800 40 51 73</p>
    <p>Level 2,<br>14 Fern Lane, Westbrook,<br>Sydney, Australia.</p>
  </div>
</div>
</body>
</html>
```